Standard Biz Card
Health Professionals
Please upload ai or eps of your logo
Kindly upload logo file in ai/eps format!
That contest is here: http://orders.markcraftplaza.example/contests/new-health-clinic-logo-biz-card
Sorry, there seem to be a misunderstandig as we thought this job was combined with the logo job. We do not have a logo yet, it is another contest going on at the moment.
Please upload the logo files

```html
<!DOCTYPE html>
<html lang="nb">
<head>
<meta charset="utf-8">
<title>Erik Solberg – Manuellterapeut</title>
<link rel="stylesheet" href="https://fonts.googleapis.com/css2?family=Tinos&family=Arimo:ital@0;1&display=swap">
<style>
  :root {
    --page: #ffffff;
    --card: #f1f1f1;
    --blue: #3ea4ef;
    --shadow: #2e3338;
    --ink: #333333;
    --white: #ffffff;
    --logo-ink: #111111;
  }
  html, body {
    margin: 0;
    width: 1200px;
    height: 691px;
    overflow: hidden;
    background: var(--page);
  }
  .card {
    position: relative;
    width: 1200px;
    height: 691px;
    background: var(--card);
    border-radius: 26px;
    overflow: hidden;
  }
  .card__bands {
    position: absolute;
    inset: 0;
    width: 1200px;
    height: 691px;
  }
  .logo-slot {
    position: absolute;
    left: 60px;
    top: 48px;
    width: 223px;
    height: 137px;
    background: var(--white);
    box-sizing: border-box;
    padding: 22px 0 0 38px;
    font-family: "Arimo", Arial, sans-serif;
    font-size: 34px;
    line-height: 42px;
    color: var(--logo-ink);
  }
  .identity {
    position: absolute;
    left: 64px;
    top: 222px;
    color: var(--white);
  }
  .identity__name {
    margin: 0;
    font-family: "Tinos", "Times New Roman", serif;
    font-weight: 400;
    font-variant: small-caps;
    font-size: 64px;
    line-height: 70px;
    letter-spacing: 2px;
  }
  .identity__role {
    margin: 2px 0 0 2px;
    font-family: "Arimo", Arial, sans-serif;
    font-style: italic;
    font-size: 26px;
  }
  .contact {
    position: absolute;
    right: 30px;
    top: 434px;
    margin: 0;
    font-family: "Tinos", "Times New Roman", serif;
    font-style: normal;
    font-variant: small-caps;
    font-size: 32px;
    line-height: 38.5px;
    letter-spacing: 1px;
    color: var(--ink);
    text-align: right;
  }
</style>
</head>
<body>
  <div class="card">
    <svg class="card__bands" viewBox="0 0 1200 691" aria-hidden="true">
      <path class="band-shadow" fill="var(--shadow)"
            d="M0,0 H1200 V96 C930,330 560,452 0,450 Z"/>
      <path class="band-blue" fill="var(--blue)"
            d="M0,0 H1200 V52 C920,300 500,448 0,442 Z"/>
    </svg>

    <div class="logo-slot">your logo<br>here</div>

    <div class="identity">
      <h1 class="identity__name">Erik Solberg</h1>
      <p class="identity__role">Manuellterapeut</p>
    </div>

    <address class="contact">
      Lindealléen 4, 4512 Strandvik<br>
      Phone : 00 00 00 00<br>
      Fax: 000 000 0000<br>
      Email: post@fjordmt.no<br>
      Web: www.fjordmt.no
    </address>
  </div>
</body>
</html>
```